Brimlock Assurance Branding Revamp

We are a consulting company, looking for a way to display and promote our brand. We have 2 sides to the business- Brimlock (financial) and Assurance (cyber security). The financial side products relate to business necessities: card processing, website design/hosting/maintenance, VoIP phone systems. The cyber security side promotes a bundled package of 4 solutions: network vulnerability scan, dark web scan, anti-ransomeware/malware software, and image-level backups. We want people to understand that partnering with Brimlock Assurance gives them “Grounded Sense of Calm” (tagline). Current badge and logos uploaded.

Target Market(s)

Small businesses

Contact Information for Business Card

Carla Whitfield, Vice President, carla@brimlockassurance.example, 555-384-9106, www.brimlockassurance.example

Requirements
Nice to have
• I do prefer the darker background for front and back

```html
<!DOCTYPE html>
<html lang="en">
<head>
<meta charset="utf-8">
<title>Brimlock Assurance Business Cards</title>
<link href="https://fonts.googleapis.com/css2?family=Poppins:wght@300;400;500;600;700&display=swap" rel="stylesheet">
<style>
  :root {
    --stage-grey: #a9a9a9;
    --page-white: #ffffff;
    --wine: #3a0003;
    --brand-red: #c8141b;
    --name-red: #8b0a0f;
    --ink: #2b2b2b;
    --ink-soft: #444444;
    --card-white: #f6f6f6;
    --rule: #2b2b2b;
  }
  * { box-sizing: border-box; margin: 0; padding: 0; }
  html, body { width: 1200px; height: 3146px; overflow: hidden; }
  body { font-family: "Poppins", sans-serif; background: var(--page-white); position: relative; }

  .stage { position: absolute; left: 0; top: 0; width: 1200px; height: 1619px; background: var(--stage-grey); }
  .sheet { position: absolute; left: 0; top: 1619px; width: 1200px; height: 1527px; background: var(--page-white); }

  .card { position: absolute; overflow: hidden; box-shadow: 0 18px 40px rgba(0,0,0,0.28); }
  .card--top { left: 185px; width: 809px; height: 462px; font-size: 8.09px; }
  .card--bottom { left: 180px; width: 839px; height: 479px; font-size: 8.39px; }

  .card-front { background: var(--wine); color: #fff; }
  .card-back { background: var(--card-white); color: var(--ink); }

  .front-brand {
    position: absolute; left: 9.7%; top: 44%;
    font-weight: 600; font-size: 3.3em; letter-spacing: 0.22em;
    color: #fff; text-transform: uppercase; white-space: nowrap;
  }
  .front-tagline {
    position: absolute; left: 9.7%; top: 66%;
    font-size: 4.5em; font-weight: 300; color: #fff; white-space: nowrap; letter-spacing: -0.01em;
  }
  .front-tagline strong { font-weight: 600; }

  .back-brand {
    position: absolute; left: 8%; width: 42%; top: 46%;
    text-align: center; font-weight: 600; font-size: 3.4em; letter-spacing: 0.18em;
    color: var(--ink); text-transform: uppercase; line-height: 1.25;
  }
  .back-divider { position: absolute; left: 50%; top: 23%; height: 46%; width: 2px; background: var(--rule); }
  .back-details { position: absolute; left: 53.3%; top: 23.5%; }
  .back-tagline { font-size: 2.6em; font-weight: 500; color: var(--ink-soft); white-space: nowrap; }
  .person-name { margin-top: 1.35em; font-size: 2.35em; font-weight: 500; color: var(--name-red); line-height: 1.2; }
  .person-title { font-size: 2.35em; font-weight: 300; color: var(--ink-soft); line-height: 1.2; }
  .contact-list { list-style: none; margin-top: 1.6em; }
  .contact-item { display: flex; align-items: center; gap: 1.3em; font-size: 1.95em; font-weight: 500; color: var(--ink-soft); line-height: 1.8; white-space: nowrap; }
  .contact-item svg { width: 1.1em; height: 1.1em; fill: var(--brand-red); flex: none; }
  .back-website {
    position: absolute; left: 0; right: 0; top: 79%;
    text-align: center; font-size: 2.55em; font-weight: 500; letter-spacing: 0.1em; color: var(--ink);
  }
</style>
</head>
<body>

<section class="stage">
  <article class="card card--top card-front" style="top:337px">
    <div class="front-brand">Brimlock Assurance</div>
    <p class="front-tagline">Grounded <strong>Sense of Calm</strong></p>
  </article>
  <article class="card card--top card-back" style="top:866px">
    <div class="back-brand">Brimlock<br>Assurance</div>
    <div class="back-divider"></div>
    <div class="back-details">
      <p class="back-tagline">Grounded Sense of Calm</p>
      <p class="person-name">Carla Whitfield,</p>
      <p class="person-title">Vice President</p>
      <ul class="contact-list">
        <li class="contact-item"><svg viewBox="0 0 24 24"><path d="M3 9c0-3 4-5 9-5s9 2 9 5v2h-5V9H8v2H3zM6 12h12l2 8H4z"/></svg>555-384-9106</li>
        <li class="contact-item"><svg viewBox="0 0 24 24"><path d="M2 6h20v13H2zM4 8v1l8 5 8-5V8l-8 5z"/></svg>carla@brimlockassurance.example</li>
      </ul>
    </div>
    <p class="back-website">www.brimlockassurance.example</p>
  </article>
</section>

<section class="sheet">
  <article class="card card--bottom card-front" style="top:214px">
    <div class="front-brand">Brimlock Assurance</div>
    <p class="front-tagline">Grounded <strong>Sense of Calm</strong></p>
  </article>
  <article class="card card--bottom card-back" style="top:765px">
    <div class="back-brand">Brimlock<br>Assurance</div>
    <div class="back-divider"></div>
    <div class="back-details">
      <p class="back-tagline">Grounded Sense of Calm</p>
      <p class="person-name">Carla Whitfield,</p>
      <p class="person-title">Vice President</p>
      <ul class="contact-list">
        <li class="contact-item"><svg viewBox="0 0 24 24"><path d="M3 9c0-3 4-5 9-5s9 2 9 5v2h-5V9H8v2H3zM6 12h12l2 8H4z"/></svg>555-384-9106</li>
        <li class="contact-item"><svg viewBox="0 0 24 24"><path d="M2 6h20v13H2zM4 8v1l8 5 8-5V8l-8 5z"/></svg>carla@brimlockassurance.example</li>
      </ul>
    </div>
    <p class="back-website">www.brimlockassurance.example</p>
  </article>
</section>

</body>
</html>
```